Tidewater Bureau for Crop Wellbeing and Harm Reduction Needs a Flyer Design

We need a flyer design template for our research, education, and prevention center housed at a major university called the "Tidewater Bureau for Crop Wellbeing and Harm Reduction (TBCWHR)." We would like to see designs that use the colors blue and white (PMS 286 (Pantone Matching System) with images that reflect farm scenes in the southeast. I've attached the TBCWHR logo, university logo and copy for the flyer. However, we are most interested in a design template that we can use again and again for new and updated information or for future flyers. This has to be a flyer that we can print on regular paper stock or glossy.
Professionals in agriculture professions; agriculture communities
University

```html
<!DOCTYPE html>
<html lang="en">
<head>
<meta charset="utf-8">
<title>Tidewater Bureau for Crop Wellbeing and Harm Reduction – Flyer</title>
<link rel="stylesheet" href="https://fonts.googleapis.com/css2?family=Roboto+Condensed:wght@700&family=Roboto:wght@400;700&display=swap">
<style>
  :root {
    --navy: #0f3d5c;
    --blue: #155ea6;
    --brand: #1f5fa8;
    --green: #8cc63f;
    --white: #ffffff;
    --sky: #eef2ee;
    --tree: #3f6a2a;
    --field: #5c9a30;
    --field-light: #86b948;
    --field-dark: #2c5619;
  }
  * { box-sizing: border-box; margin: 0; padding: 0; }
  html, body { width: 855px; height: 1200px; overflow: hidden; background: var(--white); }
  .flyer { position: relative; width: 855px; height: 1200px; font-family: "Roboto", Arial, sans-serif; }

  .hero {
    position: absolute; left: 0; top: 0; width: 855px; height: 575px;
    background:
      radial-gradient(ellipse 260px 140px at 720px 400px, rgba(140,190,80,.55), transparent 70%),
      radial-gradient(ellipse 420px 160px at 260px 300px, rgba(120,175,60,.45), transparent 70%),
      radial-gradient(ellipse 500px 120px at 600px 270px, rgba(225,235,225,.35), transparent 70%),
      radial-gradient(ellipse 300px 110px at 560px 110px, rgba(215,222,215,.55), transparent 70%),
      linear-gradient(180deg, var(--sky) 0%, #d5dfcf 8%, #5f8a3c 17%, var(--tree) 28%, #6fa23a 36%, var(--field-light) 48%, var(--field) 66%, var(--field-dark) 100%);
  }
  .hero-title {
    position: absolute; left: 66px; top: 360px;
    font-family: "Roboto Condensed", "Arial Narrow", sans-serif;
    font-weight: 700; font-size: 47px; line-height: 57px;
    color: var(--white); text-transform: uppercase; letter-spacing: 0.2px;
    text-shadow:
      -1.5px -1.5px 0 var(--brand), 1.5px -1.5px 0 var(--brand),
      -1.5px 1.5px 0 var(--brand), 1.5px 1.5px 0 var(--brand),
      3px 3px 0 var(--brand), 4.5px 4.5px 0 var(--green);
  }

  .panel { position: absolute; top: 575px; height: 461px; color: var(--white); }
  .panel-about { left: 0; width: 343px; background: var(--navy); padding: 48px 30px 0 55px; }
  .panel-facts { left: 343px; width: 512px; background: var(--blue); padding: 48px 38px 0 18px; }

  .panel-heading {
    font-family: "Roboto Condensed", "Arial Narrow", sans-serif;
    font-weight: 700; font-size: 21px; letter-spacing: 0.6px; margin-bottom: 24px;
  }
  .panel-facts .panel-heading { padding-left: 6px; margin-bottom: 28px; }
  .panel-about p { font-size: 15.5px; line-height: 20px; text-align: justify; margin-bottom: 34px; hyphens: auto; }
  .fact-list { list-style: none; }
  .fact-list li { font-size: 16px; line-height: 20px; margin-bottom: 10px; text-align: justify; }
  .fact-list li::before { content: "• "; }

  .accent-rule { position: absolute; left: 0; top: 1036px; width: 855px; height: 9px; background: var(--green); }

  .footer { position: absolute; left: 0; top: 1045px; width: 855px; height: 155px; background: var(--white); color: var(--brand); }
  .university {
    position: absolute; left: 38px; top: 32px; width: 180px; text-align: center;
    font-weight: 700; font-size: 17px; line-height: 22px; color: var(--brand);
  }
  .center-name {
    position: absolute; left: 244px; top: 20px; width: 100px;
    display: flex; flex-direction: column; align-items: center; gap: 8px;
    font-weight: 700; font-size: 16px; color: var(--brand);
  }
  .center-name .mark { width: 76px; height: 76px; border-radius: 50%; background: var(--brand); }

  .contact { position: absolute; left: 396px; top: 46px; }
  .contact-phone { display: flex; align-items: center; gap: 14px; font-weight: 700; font-size: 35px; line-height: 40px; }
  .contact-phone svg { width: 27px; height: 27px; }
  .social { display: flex; gap: 4px; margin-left: 18px; }
  .social span { width: 26px; height: 26px; background: var(--brand); }
  .contact-web { margin-top: 8px; padding-left: 30px; font-weight: 700; font-size: 18px; }
</style>
</head>
<body>
<div class="flyer">
  <section class="hero" role="img" aria-label="Photo of horses grazing in a green pasture beside a winding white wooden fence, with a white barn and trees behind">
    <h1 class="hero-title">Tidewater Bureau for<br>Crop Wellbeing and<br>Harm Reduction</h1>
  </section>

  <section class="panel panel-about">
    <h2 class="panel-heading">WHAT WE DO…</h2>
    <p>Research, education and advocacy to prevent work-related illnesses and injuries and injuries and to improve the safety and health of agricultural workers and their families in the southeastern United States.</p>
    <h2 class="panel-heading">WHO WE SERVE…</h2>
    <p>Family farmers, farm workers, large producers, professionals working in agricultural health &amp; safety, researchers and communities.</p>
  </section>

  <section class="panel panel-facts">
    <h2 class="panel-heading">DID YOU KNOW…</h2>
    <ul class="fact-list">
      <li>Agriculture ranks among the most hazardous industries.</li>
      <li>Agricultural injuries and deaths affect individuals, their families, and their communities.</li>
      <li>Many of the more than 250 persons killed each year in farming related incidents include children, youth and older workers.</li>
      <li>The annual estimated cost of agricultural injuries exceeds $4.5 billion.</li>
      <li>1 in 10 workers in agriculture, forestry and commercial fishing is injured seriously enough to require time off.</li>
      <li>Leading causes of death include tractors, machinery, motor vehicles, and electrocution.</li>
    </ul>
  </section>

  <div class="accent-rule"></div>

  <footer class="footer">
    <div class="university">Coastal Plains University<br>College of Public Health</div>
    <div class="center-name"><span class="mark"></span>TBCWHR</div>
    <div class="contact">
      <div class="contact-phone">
        <svg viewBox="0 0 26 26" aria-hidden="true">
          <rect width="26" height="26" rx="2" fill="#1f5fa8"/>
          <path d="M8.2 5.5c.6-.3 1.3 0 1.6.6l1.4 2.8c.3.6.1 1.2-.4 1.6l-1.2.9c.8 1.8 2.2 3.3 4 4.2l1-1.2c.4-.5 1.1-.6 1.6-.3l2.7 1.5c.6.3.8 1 .5 1.6l-.9 1.6c-.4.7-1.2 1.1-2 .9C10.9 18.5 7.5 15 6.3 9.4c-.2-.8.2-1.6.9-2z" fill="#ffffff"/>
        </svg>
        555.014.2290
        <div class="social" aria-hidden="true"><span></span><span></span></div>
      </div>
      <div class="contact-web">www.med.coastalplains.edu/tbcwhr</div>
    </div>
  </footer>
</div>
</body>
</html>
```